Patient Engagement Solution

We need an attractive and easy-to-use GUI for patients and clinicians, which includes screens and icons. The application has been named Quorvix. I have our corporate logo attached as well.
I have attached the screens that the developer has used to create the solution, but we all know they miss the target when it comes to the creative stuff.
If it helps, I can supply some competitor's screens as a guide - please let me know.

Target Market(s)

Patients and Clinicians

Industry/Entity Type

Healthcare/Hospitals

Font styles to use
Other font styles liked:
• Easy to Read

Requirements
Must have
• Attractive, easy to use graphical user interface. Screen size is usually 22" 16:9
Nice to have
• Inviting and interesting look
Should not have
• Complicated hard to navigate screens

```html
<!DOCTYPE html>
<html lang="en">
<head>
<meta charset="utf-8">
<title>Quorvix – Home</title>
<link href="https://fonts.googleapis.com/css2?family=Quicksand:wght@500;600;700&display=swap" rel="stylesheet">
<style>
  :root{
    --bg:#3a3a3a;
    --text:#ffffff;
    --divider:rgba(255,255,255,0.22);
    --tile:rgba(255,255,255,0.07);
    --tile-active:#232323;
    --focus:#e3151e;
    --blue-a:#27c1ef;--blue-b:#1c93c9;
    --yellow-a:#e6dc1e;--yellow-b:#bfb01a;
    --green-a:#2fd86d;--green-b:#17b24f;
    --pink-a:#f57ef3;--pink-b:#e227dc;
    --teal-a:#2fe0d2;--teal-b:#17b8ab;
    --orange-a:#f4a126;--orange-b:#d87c18;
  }
  *{margin:0;padding:0;box-sizing:border-box}
  html,body{width:1200px;height:675px;overflow:hidden;background:var(--bg)}
  body{font-family:"Quicksand",sans-serif;color:var(--text);position:relative}
  .backdrop{position:absolute;inset:0;
    background:radial-gradient(ellipse at 55% 45%,#5c5c5c 0%,#444 45%,#333 100%)}
  .header{position:absolute;left:120px;top:45px;width:960px;height:70px}
  .brand{position:absolute;left:0;top:14px;font-weight:700;font-size:34px;letter-spacing:0.5px;line-height:1.2}
  .clock{position:absolute;right:0;top:-6px;text-align:right}
  .clock-time{font-size:38px;font-weight:600;line-height:1.2;letter-spacing:1px}
  .clock-date{font-size:21px;font-weight:500;margin-top:6px}
  .divider{position:absolute;left:120px;top:142px;width:960px;height:2px;background:var(--divider)}
  .menu{position:absolute;left:120px;top:175px;display:grid;
    grid-template-columns:repeat(3,300px);grid-template-rows:repeat(2,179px);gap:30px}
  .tile{background:var(--tile);display:flex;flex-direction:column;align-items:center;padding-top:31px}
  .tile.is-focused{background:var(--tile-active);border:2px solid var(--focus);padding-top:29px}
  .tile-icon{width:75px;height:75px;border-radius:10px;display:flex;align-items:center;justify-content:center}
  .tile-icon svg{width:40px;height:40px;fill:none;stroke:#fff;stroke-width:2.2;stroke-linecap:round;stroke-linejoin:round}
  .tile-label{margin-top:18px;font-size:21px;font-weight:500;letter-spacing:0.5px}
  .icon-start{background:linear-gradient(160deg,var(--blue-a),var(--blue-b))}
  .icon-tv{background:linear-gradient(160deg,var(--yellow-a),var(--yellow-b))}
  .icon-radio{background:linear-gradient(160deg,var(--green-a),var(--green-b))}
  .icon-apps{background:linear-gradient(160deg,var(--pink-a),var(--pink-b))}
  .icon-language{background:linear-gradient(160deg,var(--teal-a),var(--teal-b))}
  .icon-clock{background:linear-gradient(160deg,var(--orange-a),var(--orange-b))}
</style>
</head>
<body>
  <div class="backdrop" role="img" aria-label="Softly blurred greyscale photo of a stethoscope resting on an open book"></div>

  <header class="header">
    <div class="brand">Quorvix</div>
    <div class="clock">
      <div class="clock-time">09:04</div>
      <div class="clock-date">Wednesday, 08 Nov 2023</div>
    </div>
  </header>
  <div class="divider"></div>

  <nav class="menu">
    <div class="tile is-focused">
      <div class="tile-icon icon-start">
        <svg viewBox="0 0 40 40"><path d="M20 5v13"/><path d="M12 10.5a13 13 0 1 0 16 0"/></svg>
      </div>
      <div class="tile-label">Start</div>
    </div>
    <div class="tile">
      <div class="tile-icon icon-tv">
        <svg viewBox="0 0 40 40"><rect x="5" y="8" width="30" height="20" rx="2"/><path d="M12 33h16"/></svg>
      </div>
      <div class="tile-label">TV</div>
    </div>
    <div class="tile">
      <div class="tile-icon icon-radio">
        <svg viewBox="0 0 40 40"><path d="M10 6l24 9"/><rect x="6" y="15" width="28" height="20" rx="3"/><circle cx="25" cy="25" r="3.5"/><path d="M12 21.5v0M12 28.5v0" stroke-width="3.4"/></svg>
      </div>
      <div class="tile-label">Radio</div>
    </div>
    <div class="tile">
      <div class="tile-icon icon-apps">
        <svg viewBox="0 0 40 40"><rect x="6" y="6" width="11" height="11" rx="2"/><rect x="23" y="6" width="11" height="11" rx="2"/><rect x="6" y="23" width="11" height="11" rx="2"/><rect x="23" y="23" width="11" height="11" rx="2"/></svg>
      </div>
      <div class="tile-label">Applications</div>
    </div>
    <div class="tile">
      <div class="tile-icon icon-language">
        <svg viewBox="0 0 40 40"><path d="M4 9h16M12 5v4M7 9q3 10 12 14M18 9q-3 10-12 14"/><path d="M22 36l6-18 6 18M24.5 29h7"/></svg>
      </div>
      <div class="tile-label">Language</div>
    </div>
    <div class="tile">
      <div class="tile-icon icon-clock">
        <svg viewBox="0 0 40 40"><circle cx="20" cy="20" r="15"/><path d="M20 11v9l6 6"/></svg>
      </div>
      <div class="tile-label">Clock</div>
    </div>
  </nav>
</body>
</html>
```